HWN Structures Ltd- building and maintenance company looking to create professional branding for m

creation of a website for a building and maintenance company,
will need a gallery and references/ reviews page
homepage to have some company information with rolling photos of completed works
all suggestions welcome on additional requirements for website.
layout should be easy to navigate.

Target Market(s)

30-70s homeowners with mid to high income

Logo Text

HWN Structures Ltd

Coding

Coded - Design and coding required

Number of Pages Required

4 page

```html
<!DOCTYPE html>
<html lang="en">
<head>
<meta charset="utf-8">
<title>HWN Structures Ltd – Building and Maintenance</title>
<link href="https://fonts.googleapis.com/css2?family=Jost:wght@300;400&family=Lato:ital,wght@0,400;0,700;0,900;1,400&display=swap" rel="stylesheet">
<style>
:root{
  --navy:#0f2b45;
  --navy-deep:#0b2238;
  --teal:#2a86a6;
  --teal-dark:#1f6f8d;
  --sky:#e6f2f9;
  --ink:#2b2b2b;
  --muted:#555d63;
  --line:#cfd8de;
  --white:#ffffff;
  --star:#f47b20;
}
*{box-sizing:border-box;margin:0;padding:0}
html,body{width:1200px;height:4918px;overflow:hidden}
body{position:relative;font-family:'Lato',sans-serif;color:var(--ink);background:var(--white)}
.abs{position:absolute}
section{position:absolute;left:0;width:1200px}
h1,h2,h3{font-family:'Jost',sans-serif;font-weight:300}

/* connector */
.connector{position:absolute;left:599px;width:2px;height:84px;background:var(--navy)}
.connector::after{content:"";position:absolute;left:-6px;bottom:-6px;width:14px;height:14px;border-radius:50%;background:var(--navy)}
.connector.light{background:var(--white)}
.connector.light::after{background:var(--navy);border:2px solid var(--white)}

/* hero */
.hero{top:0;height:797px}
.hero-photo{position:absolute;inset:0;background:linear-gradient(180deg,#5b6a78 0%,#7d858b 35%,#4b4f55 70%,#2e3136 100%)}
.hero-shade{position:absolute;inset:0;background:linear-gradient(180deg,rgba(10,25,40,.55) 0%,rgba(10,25,40,0) 22%)}
.brand{position:absolute;left:143px;top:40px;display:flex;align-items:center;gap:14px;color:var(--white);font-family:'Lato',sans-serif;font-weight:700;font-size:28px;letter-spacing:.5px}
.brand-mark{width:56px;height:56px;border-radius:50%;border:4px solid var(--white)}
.call{position:absolute;left:483px;top:32px;display:flex;gap:10px;color:var(--white)}
.call small{display:block;font-size:12px;font-weight:700;letter-spacing:.5px}
.call strong{display:block;font-size:20px;font-weight:900;letter-spacing:.5px}
.btn-quote{position:absolute;left:710px;top:32px;width:185px;height:39px;border-radius:20px;background:var(--teal);color:var(--white);font-size:13px;font-weight:700;letter-spacing:.5px;display:flex;align-items:center;justify-content:center}
.social-top{position:absolute;left:922px;top:34px;display:flex;gap:12px}
.social-top span{width:36px;height:36px;border-radius:50%;border:2px solid var(--white)}
.nav{position:absolute;left:433px;top:100px;display:flex;gap:26px;font-size:14px;font-weight:700;color:var(--white);letter-spacing:.3px}
.nav .active{border-bottom:2px solid var(--white);padding-bottom:2px}
.hero-box{position:absolute;left:340px;top:300px;width:522px;height:278px;border-radius:14px;background:rgba(18,28,40,.72);text-align:center;color:var(--white)}
.hero-box h1{font-size:60px;margin-top:42px;line-height:1}
.hero-box p{font-size:19px;font-weight:700;line-height:27px;margin-top:22px}
.btn-learn{display:inline-flex;align-items:center;justify-content:center;width:168px;height:46px;margin-top:20px;border-radius:24px;background:var(--teal);font-size:14px;font-weight:700;letter-spacing:.5px}
.arrow{position:absolute;top:414px;width:32px;height:32px;border-radius:50%;background:rgba(255,255,255,.85)}

/* welcome */
.welcome{top:797px;height:691px;background:linear-gradient(115deg,#fff 40%,#f3f6f8 60%,#fff 80%)}
.welcome-frame{position:absolute;left:137px;top:157px;width:460px;height:435px;border:3px solid var(--teal);border-radius:14px}
.welcome-photo{position:absolute;left:137px;top:161px;width:447px;height:426px;border-radius:12px;background:linear-gradient(135deg,#3b4048 0%,#7a6d62 45%,#d9935a 65%,#4a4e56 100%)}
.welcome-text{position:absolute;left:654px;top:170px;width:420px}
.welcome-text h2{font-size:33px;line-height:46px;color:var(--navy)}
.welcome-text h2 span{display:block;font-size:38px}
.welcome-text p{font-size:14px;line-height:22.4px;color:var(--muted);margin-top:20px}
.btn-outline{display:inline-flex;align-items:center;justify-content:center;width:140px;height:38px;margin-top:30px;border:2px solid var(--navy);border-radius:3px;font-size:14px;font-weight:900;color:var(--navy)}

/* services */
.services{top:1488px;height:1006px;background:linear-gradient(160deg,#4b8fb1 0%,#2e6d92 40%,#1b4d72 75%,#163e5d 100%)}
.services-title{position:absolute;top:130px;width:100%;text-align:center;font-size:40px;color:var(--white)}
.card{position:absolute;width:296px;height:328px;background:var(--white);text-align:center;padding:34px 22px 0}
.card.shift{height:330px}
.card-icon{width:108px;height:108px;margin:0 auto;border-radius:50%;background:var(--teal);border:3px solid var(--white);box-shadow:0 0 0 2px var(--teal);display:flex;align-items:center;justify-content:center}
.card h3{font-size:19px;line-height:22px;color:var(--ink);font-weight:400;margin-top:16px}
.card p{font-size:13px;line-height:22px;color:var(--muted);margin-top:12px}

/* gallery */
.gallery{top:2494px;height:914px}
.gallery-title{position:absolute;top:100px;width:100%;text-align:center;font-size:40px;color:var(--ink)}
.tile{position:absolute}
.tile-label{position:absolute;left:0;right:0;top:266px;text-align:center;color:var(--white);font-family:'Jost',sans-serif;font-size:24px;line-height:30px}

/* testimonial */
.testimonials{top:3408px;height:784px}
.testimonials-title{position:absolute;top:105px;width:100%;text-align:center;font-size:40px}
.quote{position:absolute;top:217px;width:285px}
.bubble{position:absolute;left:0;top:0}
.quote p{position:absolute;left:22px;top:28px;width:241px;text-align:center;font-style:italic;font-size:13.5px;line-height:22.4px;color:var(--muted)}
.author{position:absolute;left:11px;top:362px;display:flex;align-items:center;gap:18px}
.avatar{width:92px;height:92px;border-radius:50%;background:linear-gradient(160deg,#c7d2dc,#33445a);border:3px solid #e2e7ea}
.author b{display:block;font-size:12px;font-weight:900;line-height:20px}
.stars{display:flex;gap:3px;margin-top:4px}

/* contact */
.contact{top:4192px;height:726px}
.contact-bg{position:absolute;left:0;top:0;width:1200px;height:560px;background:linear-gradient(180deg,#2a4d6e 0%,#1e3f60 60%,#16334f 100%)}
.contact-title{position:absolute;top:120px;width:100%;text-align:center;color:var(--white);font-size:40px}
.contact-box{position:absolute;left:145px;top:213px;width:910px;height:365px;background:var(--white);border:1px solid var(--line)}
.contact-form{position:absolute;left:0;top:0;width:572px;height:100%;background:var(--sky)}
.field{position:absolute;height:46px;background:var(--white);border:1px solid var(--line);border-radius:3px;font-size:13px;color:var(--muted);padding:14px 18px}
.btn-submit{position:absolute;left:29px;top:281px;width:151px;height:42px;background:var(--navy);color:var(--white);font-size:14px;font-weight:900;display:flex;align-items:center;justify-content:center;letter-spacing:.5px}
.info{position:absolute;left:599px;display:flex;gap:18px;font-size:13px;line-height:19px;color:var(--muted)}
.info-icon{width:38px;height:38px;border-radius:50%;border:2px solid var(--navy);flex:none;display:flex;align-items:center;justify-content:center}
.social-contact{position:absolute;left:609px;top:262px;display:flex;gap:10px}
.social-contact span{width:36px;height:36px;border-radius:50%;border:2px solid var(--navy)}
.footer{position:absolute;top:650px;width:100%;text-align:center;font-size:15px;color:var(--ink)}
</style>
</head>
<body>

<!-- HERO -->
<section class="hero">
  <div class="hero-photo" role="img" aria-label="Photo of a construction worker in hard hat and hi-vis vest carrying a ladder and toolbox on a building site"></div>
  <div class="hero-shade"></div>
  <div class="brand"><span class="brand-mark"></span>HWN Structures</div>
  <div class="call">
    <svg width="34" height="34" viewBox="0 0 24 24" fill="none" stroke="#fff" stroke-width="1.8"><path d="M5 3h4l2 5-2.5 1.5a11 11 0 0 0 6 6L16 13l5 2v4a2 2 0 0 1-2 2A16 16 0 0 1 3 5a2 2 0 0 1 2-2z"/></svg>
    <div><small>CALL US</small><strong>555-0100-0142</strong></div>
  </div>
  <div class="btn-quote">REQUEST A QUOTE</div>
  <div class="social-top"><span></span><span></span><span></span></div>
  <nav class="nav">
    <span class="active">HOME</span><span>ABOUT US</span><span>OUR SERVICES</span><span>GALLERY</span><span>TESTIMONIAL</span><span>CONTACT</span>
  </nav>
  <div class="hero-box">
    <h1>HWN Structures</h1>
    <p>Nemo enim ipsam voluptatem quia voluptas<br>sit aspernatur aut odit aut</p>
    <span class="btn-learn">LEARN MORE</span>
  </div>
  <div class="arrow" style="left:58px"><svg width="32" height="32" viewBox="0 0 32 32"><path d="M18 10l-6 6 6 6" fill="none" stroke="#222" stroke-width="2.5"/></svg></div>
  <div class="arrow" style="left:1108px"><svg width="32" height="32" viewBox="0 0 32 32"><path d="M14 10l6 6-6 6" fill="none" stroke="#222" stroke-width="2.5"/></svg></div>
</section>

<!-- WELCOME -->
<section class="welcome">
  <div class="connector" style="top:0"></div>
  <div class="welcome-frame"></div>
  <div class="welcome-photo" role="img" aria-label="Photo of a worker in hi-vis vest inside a steel-framed building under construction"></div>
  <div class="welcome-text">
    <h2>Welcome to<span>HWN Structures Ltd</span></h2>
    <p>Sed ut perspiciatis unde omnis iste natus error sit voluptatem accusantium doloremque laudantium, totam rem aperiam, eaque ipsa quae ab illo inventore veritatis et quasi architecto beatae vitae dicta sunt explicabo. Nemo enim ipsam voluptatem quia voluptas sit aspernatur aut odit aut fugit, sed quia consequuntur magni dolores eos qui ratione voluptatem sequi nesciunt. Neque porro quisquam Sed ut perspiciatis unde omnis iste natus error sit voluptatem accusantium doloremque laudantium, totam rem aperiam, eaque ipsa quae ab illo inventore</p>
    <span class="btn-outline">READ MORE</span>
  </div>
</section>

<!-- SERVICES -->
<section class="services" role="img" aria-label="Blue-tinted background photo of steel scaffolding and site workers">
  <div class="connector light" style="top:0"></div>
  <h2 class="services-title">Building and Maintenance</h2>

  <div class="card" style="left:145px;top:218px">
    <div class="card-icon"><svg width="56" height="56" viewBox="0 0 56 56" fill="none" stroke="#fff" stroke-width="2"><rect x="10" y="8" width="36" height="40"/><path d="M18 16h6M32 16h6M18 26h6M32 26h6M18 36h6M32 36h6"/></svg></div>
    <h3>Nemo enim ipsam</h3>
    <p>Sed ut perspiciatis unde omnis iste natussit voluptatem accusantium doloremque laudantium, totam rem aperiam, eaque ipsa</p>
  </div>
  <div class="card shift" style="left:452px;top:233px">
    <div class="card-icon"><svg width="56" height="56" viewBox="0 0 56 56" fill="none" stroke="#fff" stroke-width="2"><circle cx="28" cy="20" r="9"/><path d="M12 46c0-9 7-14 16-14s16 5 16 14"/><path d="M17 20a11 11 0 0 1 22 0"/></svg></div>
    <h3>24-Hr Service calls for<br>maintenance works</h3>
    <p>Sed ut perspiciatis unde omnis iste natussit voluptatem accusantium doloremque laudantium, totam rem</p>
  </div>
  <div class="card" style="left:759px;top:218px">
    <div class="card-icon"><svg width="56" height="56" viewBox="0 0 56 56" fill="none" stroke="#fff" stroke-width="2"><rect x="8" y="10" width="20" height="16"/><rect x="26" y="24" width="22" height="22"/><path d="M32 30h4M40 30h4M32 38h4M40 38h4"/></svg></div>
    <h3>HWN Structures</h3>
    <p>Sed ut perspiciatis unde omnis iste natussit voluptatem accusantium doloremque laudantium, totam rem aperiam, eaque ipsa</p>
  </div>

  <div class="card" style="left:145px;top:555px">
    <div class="card-icon"><svg width="56" height="56" viewBox="0 0 56 56" fill="none" stroke="#fff" stroke-width="2"><rect x="10" y="14" width="32" height="32" transform="rotate(-20 26 30)"/><path d="M36 8l10 10-16 16-10-10z"/></svg></div>
    <h3>Design and construct</h3>
    <p>Sed ut perspiciatis unde omnis iste natussit voluptatem accusantium doloremque laudantium, totam rem aperiam, eaque ipsa</p>
  </div>
  <div class="card shift" style="left:452px;top:571px">
    <div class="card-icon"><svg width="56" height="56" viewBox="0 0 56 56" fill="none" stroke="#fff" stroke-width="2"><path d="M16 22a12 12 0 0 1 24 0z"/><path d="M12 22h32"/><path d="M16 48c0-8 5-12 12-12s12 4 12 12"/></svg></div>
    <h3>Construction</h3>
    <p>Sed ut perspiciatis unde omnis iste natussit voluptatem accusantium doloremque laudantium, totam rem aperiam, eaque ipsa</p>
  </div>
  <div class="card" style="left:759px;top:555px">
    <div class="card-icon"><svg width="56" height="56" viewBox="0 0 56 56" fill="none" stroke="#fff" stroke-width="2"><circle cx="24" cy="22" r="10"/><path d="M8 48c0-9 7-14 16-14"/><rect x="32" y="32" width="16" height="16"/></svg></div>
    <h3>Project Management</h3>
    <p>Sed ut perspiciatis unde omnis iste natussit voluptatem accusantium doloremque laudantium, totam rem aperiam, eaque ipsa</p>
  </div>
</section>

<!-- GALLERY -->
<section class="gallery">
  <div class="connector" style="top:0"></div>
  <h2 class="gallery-title">Our Gallery</h2>
  <div class="tile" style="left:0;top:206px;width:435px;height:347px;background:linear-gradient(150deg,#9fb0bf,#5b6c7c 60%,#3d4650)" role="img" aria-label="Photo of a site worker in hard hat and hi-vis vest looking at a building"></div>
  <div class="tile" style="left:446px;top:206px;width:371px;height:347px;background:linear-gradient(180deg,#8b8f93,#4e4a47 55%,#2a2623)" role="img" aria-label="Photo of a worker between tall industrial cladding panels">
    <div class="tile-label">Building &amp; Maintenance<br>&rarr;</div>
  </div>
  <div class="tile" style="left:828px;top:206px;width:372px;height:347px;background:linear-gradient(160deg,#2a2a33,#a2583a 55%,#e4893a 75%,#1e1b1d)" role="img" aria-label="Photo of silhouetted workers on a steel structure at sunset"></div>
  <div class="tile" style="left:0;top:566px;width:435px;height:348px;background:linear-gradient(135deg,#d8d6d0,#8d98a3 50%,#3c4c62)" role="img" aria-label="Photo of two workers fitting plasterboard on a ceiling"></div>
  <div class="tile" style="left:446px;top:566px;width:754px;height:348px;background:linear-gradient(120deg,#d9e2ea,#9fb6cb 40%,#9ab040 75%,#c56a2e)" role="img" aria-label="Photo of workers in hi-vis gear on a steel frame under a blue sky"></div>
</section>

<!-- TESTIMONIAL -->
<section class="testimonials">
  <div class="connector" style="top:0"></div>
  <h2 class="testimonials-title">Testimonial</h2>

  <div class="quote" style="left:137px">
    <svg class="bubble" width="285" height="330" viewBox="0 0 285 330"><path d="M20 1h245a19 19 0 0 1 19 19v266a19 19 0 0 1-19 19H247l-55 24 14-24H20a19 19 0 0 1-19-19V20A19 19 0 0 1 20 1z" fill="#fff" stroke="#b9c2c8" stroke-width="1.5"/></svg>
    <p>Sed ut perspiciatis unde omnis iste natus error sit voluptatem accntium doloremque laudantium, totam rem aperiam, eaque ipsa quae ab illo intore veritatis et quasi architecto beatae vitae dicta sunt explicabo. Nemo enim ipsam voluptatem quia voluptas sit aspernatur aut odit aut fugit, sed quia consequuntur magni dolores eos qui ratione voluptatem sequi nesciunt.</p>
    <div class="author"><div class="avatar" role="img" aria-label="Portrait photo of reviewer"></div><div><b>SAM CARTER</b><b>HWN STRUCTURES LTD</b><div class="stars"><svg width="90" height="14" viewBox="0 0 90 14" fill="#f47b20"><path id="s1" d="M7 0l2 5h5l-4 3 2 5-5-3-5 3 2-5-4-3h5z"/><use href="#s1" x="19"/><use href="#s1" x="38"/><use href="#s1" x="57"/><use href="#s1" x="76"/></svg></div></div></div>
  </div>

  <div class="quote" style="left:461px">
    <svg class="bubble" width="285" height="330" viewBox="0 0 285 330"><path d="M20 1h245a19 19 0 0 1 19 19v266a19 19 0 0 1-19 19H247l-55 24 14-24H20a19 19 0 0 1-19-19V20A19 19 0 0 1 20 1z" fill="#fff" stroke="#b9c2c8" stroke-width="1.5"/></svg>
    <p>Sed ut perspiciatis unde omnis iste natus error sit voluptatem accntium doloremque laudantium, totam rem aperiam, eaque ipsa quae ab illo intore veritatis et quasi architecto beatae vitae dicta sunt explicabo. Nemo enim ipsam voluptatem quia voluptas sit aspernatur aut odit aut fugit, sed quia consequuntur magni dolores eos qui ratione voluptatem sequi nesciunt.</p>
    <div class="author"><div class="avatar" role="img" aria-label="Portrait photo of reviewer"></div><div><b>SAM CARTER</b><b>HWN STRUCTURES LTD</b><div class="stars"><svg width="90" height="14" viewBox="0 0 90 14" fill="#f47b20"><use href="#s1"/><use href="#s1" x="19"/><use href="#s1" x="38"/><use href="#s1" x="57"/><use href="#s1" x="76"/></svg></div></div></div>
  </div>

  <div class="quote" style="left:784px">
    <svg class="bubble" width="285" height="330" viewBox="0 0 285 330"><path d="M20 1h245a19 19 0 0 1 19 19v266a19 19 0 0 1-19 19H247l-55 24 14-24H20a19 19 0 0 1-19-19V20A19 19 0 0 1 20 1z" fill="#fff" stroke="#b9c2c8" stroke-width="1.5"/></svg>
    <p>Sed ut perspiciatis unde omnis iste natus error sit voluptatem accntium doloremque laudantium, totam rem aperiam, eaque ipsa quae ab illo intore veritatis et quasi architecto beatae vitae dicta sunt explicabo. Nemo enim ipsam voluptatem quia voluptas sit aspernatur aut odit aut fugit, sed quia consequuntur magni dolores eos qui ratione voluptatem sequi nesciunt.</p>
    <div class="author"><div class="avatar" role="img" aria-label="Portrait photo of reviewer"></div><div><b>SAM CARTER</b><b>HWN STRUCTURES LTD</b><div class="stars"><svg width="90" height="14" viewBox="0 0 90 14" fill="#f47b20"><use href="#s1"/><use href="#s1" x="19"/><use href="#s1" x="38"/><use href="#s1" x="57"/><use href="#s1" x="76"/></svg></div></div></div>
  </div>
</section>

<!-- CONTACT -->
<section class="contact">
  <div class="contact-bg" role="img" aria-label="Dark blue-tinted photo of workers in hard hats"></div>
  <svg class="abs" style="left:0;top:380px" width="1200" height="190" viewBox="0 0 1200 190"><path d="M0 120Q300 60 600 150Q900 60 1200 120V190H0z" fill="#fff"/></svg>
  <div class="connector light" style="top:0"></div>
  <h2 class="contact-title">Contact Us</h2>
  <div class="contact-box">
    <div class="contact-form">
      <div class="field" style="left:29px;top:54px;width:251px">First name</div>
      <div class="field" style="left:294px;top:54px;width:250px">Last Name</div>
      <div class="field" style="left:29px;top:111px;width:251px">Email</div>
      <div class="field" style="left:294px;top:111px;width:250px">Phone Number</div>
      <div class="field" style="left:29px;top:166px;width:515px;height:96px">Message</div>
      <div class="btn-submit">SUBMIT</div>
    </div>
    <div class="info" style="top:50px">
      <span class="info-icon"><svg width="18" height="18" viewBox="0 0 24 24" fill="none" stroke="#0f2b45" stroke-width="2.2"><path d="M12 22s7-7 7-12a7 7 0 0 0-14 0c0 5 7 12 7 12z"/><circle cx="12" cy="10" r="2.5"/></svg></span>
      <div>Address<br>4385 enim ipsam voluptatem<br>quia voluptas sit</div>
    </div>
    <div class="info" style="top:127px">
      <span class="info-icon"><svg width="18" height="18" viewBox="0 0 24 24" fill="none" stroke="#0f2b45" stroke-width="2.2"><path d="M5 3h4l2 5-2.5 1.5a11 11 0 0 0 6 6L16 13l5 2v4a2 2 0 0 1-2 2A16 16 0 0 1 3 5a2 2 0 0 1 2-2z"/></svg></span>
      <div>Toll Free Phone<br>(800) 555-0123</div>
    </div>
    <div class="info" style="top:184px">
      <span class="info-icon"><svg width="18" height="18" viewBox="0 0 24 24" fill="none" stroke="#0f2b45" stroke-width="2.2"><rect x="3" y="5" width="18" height="14" rx="2"/><path d="M3 7l9 6 9-6"/></svg></span>
      <div>Email<br>info@hwnstructures.com</div>
    </div>
    <div class="social-contact"><span></span><span></span><span></span><span></span></div>
  </div>
  <p class="footer">Copyright © HWN Structures Ltd 2021. All rights reserved. | Privacy Policy</p>
</section>

</body>
</html>
```